Clean Plinth Ads Banner Design For A Finance Company

Hi,
We're a UK based finance company and are looking for new banner ads to use on the Plinth Display Network.
We want the end product to stand out by using strong, minimal design - ideally starting from a dark theme, although I'm open to ideas.
The copy should read:
'Fast Bridging Loans From 0.39% PM'
Once we have these designs agreed, we are looking to replicate them for other products, changing only the text on each ad - for example, 'commercial mortgage service you can rely on' or 'development finance service you can rely on'.
The colours used on our website are the following:
Black - #040303
Orange - #f79124
White - #ffffff
Grey - #ffffff
Example ads that I like - https://www.brimcastle.com/wp-content/uploads/2021/07/plinth-display-ads-example-2-final.png.webp
2 - https://quendrahub.com/wp-content/uploads/2020/03/fbdd56ba3bd16c7a8debb13a411de786.jpg

```html
<!DOCTYPE html>
<html lang="en">
<head>
<meta charset="utf-8">
<title>Kestrel Finance – Fast Bridging Loans</title>
<link rel="stylesheet" href="https://fonts.googleapis.com/css2?family=Montserrat:wght@500;700;800;900&display=swap">
<style>
  :root {
    --black: #040303;
    --ink: #070909;
    --orange: #f79124;
    --white: #ffffff;
    --band-1: #3a2a1b;
    --band-2: #5e401f;
    --band-3: #8e5c25;
  }
  html, body {
    margin: 0;
    padding: 0;
    width: 1200px;
    height: 233px;
    overflow: hidden;
    background: var(--black);
  }
  .banner {
    position: relative;
    width: 1200px;
    height: 233px;
    overflow: hidden;
    background: var(--orange);
    font-family: "Montserrat", sans-serif;
  }
  .chevrons {
    position: absolute;
    inset: 0;
    width: 1200px;
    height: 233px;
  }
  .brand {
    position: absolute;
    left: 19px;
    top: 54px;
    width: 243px;
    height: 114px;
    background: var(--black);
    display: flex;
    align-items: center;
    justify-content: center;
  }
  .brand-name {
    margin: 0;
    color: var(--orange);
    font-weight: 700;
    font-size: 27px;
    line-height: 1.1;
    text-align: center;
  }
  .headline { margin: 0; }
  .headline span {
    position: absolute;
    left: 404px;
    line-height: 1;
    color: var(--white);
    white-space: nowrap;
  }
  .headline .fast { top: 30px; font-size: 64px; font-weight: 800; letter-spacing: -1px; }
  .headline .bridging { top: 99px; font-size: 35px; font-weight: 500; letter-spacing: 3.6px; }
  .headline .loans { top: 138px; font-size: 56px; font-weight: 800; letter-spacing: -1px; }
  .rule {
    position: absolute;
    left: 404px;
    width: 201px;
    height: 2px;
    background: var(--white);
  }
  .rule-top { top: 94px; }
  .rule-bottom { top: 139px; }
  .rate {
    position: absolute;
    left: 616px;
    top: 0;
    margin: 0;
    font-size: 222px;
    font-weight: 800;
    line-height: 1;
    letter-spacing: -10px;
    white-space: nowrap;
    transform: scaleX(0.88);
    transform-origin: left top;
  }
  .rate-outline {
    position: absolute;
    left: -5px;
    top: -5px;
    color: transparent;
    -webkit-text-stroke: 1.5px var(--white);
  }
  .rate-value {
    position: relative;
    color: var(--ink);
  }
  .rate-unit {
    position: absolute;
    color: var(--white);
    line-height: 1;
    font-weight: 800;
  }
  .percent { left: 1042px; top: 25px; font-size: 75px; }
  .per-month { left: 1045px; top: 118px; font-size: 76px; letter-spacing: -1px; }
</style>
</head>
<body>
  <div class="banner">
    <svg class="chevrons" viewBox="0 0 1200 233" aria-hidden="true">
      <rect x="0" y="0" width="375" height="233" fill="var(--black)"/>
      <polygon points="319,0 375,0 375,233 319,233 269,116.5" fill="var(--band-1)"/>
      <polygon points="337,0 375,0 375,233 337,233 288,116.5" fill="var(--band-2)"/>
      <polygon points="356,0 375,0 375,233 356,233 306,116.5" fill="var(--band-3)"/>
      <polygon points="375,0 1200,0 1200,233 375,233 322,116.5" fill="var(--orange)"/>
    </svg>

    <div class="brand">
      <p class="brand-name">Kestrel Finance<br>Limited</p>
    </div>

    <h1 class="headline">
      <span class="fast">FAST</span>
      <span class="bridging">BRIDGING</span>
      <span class="loans">LOANS</span>
    </h1>
    <div class="rule rule-top"></div>
    <div class="rule rule-bottom"></div>

    <p class="rate">
      <span class="rate-outline" aria-hidden="true">0.39</span>
      <span class="rate-value">0.39</span>
    </p>
    <span class="rate-unit percent">%</span>
    <span class="rate-unit per-month">PM</span>
  </div>
</body>
</html>
```